Systemischer Coach sucht Flyer-Design
Zielgruppe
Ich bin systemischer Coach und gebe Einzelcoaching in einem sehr schönen Coaching Raum in Aachen.
Meine Zielgruppe sind Menschen im Alter von 28-50, die ehrgeizig, selbstbestimmt und modern sind und sich gerne weiterentwickeln möchten.
Zentrale Themen sind:
Motivation
Persönlichkeitsentwicklung
Ziel- und Entscheidungsfindung
Selbst-/Zeitmanagement
Selbstbewusstsein stärken
Work-Life-Balance
Stressmanagement
Coaching ist professioneller, individueller Begleitprozess für Menschen in herausfordernden Berufs- und Lebenssituationen. Im Rahmen eines systemischen und humanistischen Verständnisses wird der Klient dabei unterstützt, eigenständig konstruktive und nachhaltige Lösungen zu erarbeiten. Das Coaching findet in geschütztem Rahmen statt, Coach und Klient begegnen sich auf Augenhöhe. Der Klient ist Experte für die Inhalte, der Coach ist Experte für Prozess und Struktur
Aufgabenstellung
Farben
schwarz/gold
Vorderseite schlichte/kräftige Symbole und Motto 'Feel the flow'
Rückseite: Text
Text:
'Feel the Flow'
Ist es Zeit,
Deine Stärken zu entdecken?
Deine Ressourcen zu reaktivieren?
Work und Life wieder in Balance zu bringen?
für etwas mehr Motivation und Inspiration?
Suchst Du,
Mut, um Deine Ziele zu erreichen?
Wege, um den Stress links liegen zu lassen?
Selbstbewusstsein für ein sicheres Auftreten?
Struktur und Klarheit im Job?
Bring Flow in Dein Leben!
Als Coach begleite ich Dich auf Deinem Weg zum Ziel

```html
<!DOCTYPE html>
<html lang="de">
<head>
<meta charset="utf-8">
<title>Coaching Flyer</title>
<link rel="stylesheet" href="https://fonts.googleapis.com/css2?family=Montserrat:wght@200;300;700&family=Sacramento&display=swap">
<style>
  :root {
    --frame: #282828;
    --panel: #121212;
    --gold: #d9a75a;
    --gold-dark: #b9792c;
    --gold-light: #f6cd7c;
    --rule: #e0ae62;
  }
  * { margin: 0; padding: 0; box-sizing: border-box; }
  html, body {
    width: 1200px;
    height: 444px;
    overflow: hidden;
    background: var(--frame);
  }
  .flyer {
    position: absolute;
    left: 12px;
    top: 16px;
    width: 1169px;
    height: 412px;
    background: var(--panel);
  }
  .questions {
    position: absolute;
    left: 58px;
    top: 23px;
    font-family: "Montserrat", Arial, sans-serif;
    font-weight: 300;
    font-size: 20.5px;
    line-height: 27px;
    letter-spacing: 1.4px;
    color: var(--gold);
    white-space: nowrap;
  }
  .questions p + p { margin-top: 26px; }
  .motto {
    position: absolute;
    left: 56px;
    top: 340px;
    font-family: "Sacramento", cursive;
    font-size: 42px;
    line-height: 1;
    color: var(--gold);
    white-space: nowrap;
  }
  .divider {
    position: absolute;
    left: 623px;
    top: 30px;
    width: 2px;
    height: 350px;
    background: var(--rule);
  }
  .headline {
    position: absolute;
    right: 40px;
    top: 15px;
    text-align: right;
    font-family: "Montserrat", Arial, sans-serif;
    font-weight: 700;
    font-size: 59px;
    line-height: 74px;
    letter-spacing: 2px;
    text-transform: uppercase;
    white-space: nowrap;
    background: linear-gradient(100deg, var(--gold-dark) 0%, var(--gold-light) 55%, #e8b466 100%);
    -webkit-background-clip: text;
    background-clip: text;
    color: transparent;
  }
</style>
</head>
<body>
  <main class="flyer">
    <div class="questions">
      <p>Ist es Zeit,<br>
        Deine Stärken zu entdecken?<br>
        Deine Ressourcen zu reaktivieren?<br>
        Work und Life wieder in Balance zu bringen?<br>
        für etwas mehr Motivation und Inspiration?</p>
      <p>Suchst Du,<br>
        Mut, um Deine Ziele zu erreichen?<br>
        Wege, um den Stress links liegen zu lassen?<br>
        Selbstbewusstsein für ein sicheres Auftreten?<br>
        Struktur und Klarheit im Job?</p>
    </div>
    <p class="motto">Bring Flow in Dein Leben!</p>
    <div class="divider"></div>
    <h1 class="headline">Als Coach<br>begleite ich<br>dich auf<br>deinem Weg<br>zum Ziel</h1>
  </main>
</body>
</html>
```